Media/PR business needs a website upgrade

Modernise my website www.vrl.net.au into a simpler and mobile friendly site with the usual plugins, maximum 5 pages, 4 might be enough. My page is already hosted and I have an email address so I just want to work with a designer who is fantastic with WordPress, to refresh and simplify the 6 year-old look.

Target Market(s)

men & women 25-55

Industry/Entity Type

Business

Coding

Coded - Design and coding required

Number of Pages Required

4 page

Font styles to use
Sans Serif

Colors
f37122
ffffff

Requirements
Must have
• Social media plugins, about, client portfolio, contact (can be under about)blog capability
Nice to have
• photos of jobs I've done
Should not have
• e-commerce, can lose all the client logos

```html
<!DOCTYPE html>
<html lang="en">
<head>
<meta charset="utf-8">
<title>Vantage Relations</title>
<link href="https://fonts.googleapis.com/css2?family=Dosis:wght@300;400;500&family=Open+Sans:wght@400;600&display=swap" rel="stylesheet">
<style>
:root{
  --orange:#f37122;
  --orange-bright:#f7941d;
  --dark:#333333;
  --white:#ffffff;
  --text:#555555;
  --muted:#9a9a9a;
  --nav-top:#e4e4e4;
  --nav-bottom:#a9a9a9;
}
*{box-sizing:border-box;margin:0;padding:0}
html,body{width:1200px;height:1200px;overflow:hidden;background:var(--white)}
body{font-family:"Open Sans",Arial,sans-serif}
.stage{position:absolute;left:200px;top:10px;width:889px;height:1310px;transform:scale(.9);transform-origin:0 0;background:var(--dark);overflow:hidden}
.abs{position:absolute}

/* header */
.brand{left:89px;top:18px;color:var(--white);font-family:"Open Sans",sans-serif;font-weight:400;font-size:11px;line-height:11px}
.phone{right:90px;top:18px;display:flex;align-items:center;gap:4px;color:#c8c8c8;font-family:"Dosis",sans-serif;font-size:14px}
.phone-icon{width:24px;height:24px;border-radius:50%;background:#6a6a6a;display:flex;align-items:center;justify-content:center}

/* nav */
.nav{left:89px;top:63px;width:711px;height:38px;background:linear-gradient(var(--nav-top),var(--nav-bottom));display:flex;align-items:center;padding-left:8px}
.nav a{font-family:"Dosis",sans-serif;font-size:9px;color:var(--white);text-decoration:none;text-transform:uppercase;padding:7px 12px;margin-right:4px;letter-spacing:.2px}
.nav a.active{border:1px solid #c9c9c9;background:#9f9f9f}
.social{position:absolute;right:8px;top:7px;display:flex;gap:7px}
.social span{width:24px;height:24px;border-radius:50%;background:var(--dark);color:var(--white);font-size:9px;font-weight:600;display:flex;align-items:center;justify-content:center}

/* hero */
.hero-photo{left:89px;top:107px;width:160px;height:224px;background:linear-gradient(160deg,#d8d3c8,#9a9790 55%,#2f73b8 56%,#1e5d9e)}
.hero-lead{left:249px;top:107px;width:291px;height:96px;background:var(--dark);padding:14px 21px 0}
.hero-lead h1{font-family:"Dosis",sans-serif;font-weight:300;font-size:17.5px;line-height:17.5px;color:var(--white);text-transform:uppercase}
.hero-lead h1 b{font-weight:400}
.hero-copy{left:249px;top:203px;width:291px;height:128px;background:var(--orange-bright);padding:10px 20px 0;color:var(--white);font-size:7.2px;line-height:9.6px}
.hero-copy p{margin-bottom:6px;text-align:justify}

/* page widget */
.widget{left:540px;top:107px;width:260px;height:224px;background:var(--white);overflow:hidden}
.widget-cover{height:96px;background:linear-gradient(180deg,#6f9bd1,#3f6ea8 60%,#c9d4dc);position:relative}
.widget-avatar{position:absolute;left:9px;top:11px;width:38px;height:38px;border:2px solid var(--white);background:#c9a77f}
.widget-title{position:absolute;left:54px;top:10px;color:var(--white);font-family:"Dosis",sans-serif;font-weight:500;font-size:13px}
.widget-likes{position:absolute;left:54px;top:25px;color:var(--white);font-size:7.5px}
.widget-btn{position:absolute;bottom:10px;background:#f3f3f3;color:#4b4f56;font-size:7px;padding:2px 6px;border:1px solid #ccc}
.widget-body{padding:8px 10px;color:var(--text);font-size:6.5px;position:relative}
.friends{display:flex;gap:2px;margin:4px 0 8px}
.friends i{width:22px;height:20px;background:linear-gradient(#9aa8b8,#5b6b7c)}
.post{display:flex;gap:8px;align-items:flex-start}
.post-avatar{width:34px;height:34px;background:#c9a77f}
.post-name{font-family:"Dosis",sans-serif;font-size:11px;color:#333;margin-top:4px}
.post-sq{position:absolute;right:12px;top:56px;width:11px;height:11px;background:#3b5998}
.post-text{margin-top:5px;font-size:6.6px;line-height:8.6px;text-align:justify}
.widget-scroll{position:absolute;right:2px;top:98px;width:4px;height:55px;background:#c1c1c1}

/* about */
.about{left:89px;top:336px;width:242px;height:217px;background:var(--orange-bright)}
.tab{position:absolute;background:var(--dark);color:var(--white);font-family:"Dosis",sans-serif;font-weight:400;font-size:14px;padding:0 7px 4px;display:flex;align-items:flex-end}
.about .tab{left:20px;top:0;height:38px}
.about-text{position:absolute;left:22px;top:46px;width:182px;height:164px;overflow:hidden;color:var(--white);font-size:7.2px;line-height:9.6px;text-align:justify}
.about-text p{margin-bottom:4px}
.scrollbar{position:absolute;width:4px;background:rgba(255,255,255,.35)}
.scrollbar::before{content:"";position:absolute;left:0;top:0;width:4px;height:60%;background:var(--white)}
.slider{left:331px;top:336px;width:469px;height:217px;background:linear-gradient(180deg,#2f6d3f 0%,#c9c6c0 35%,#8e939a 60%,#3a3e45 100%)}
.arrow{position:absolute;top:94px;width:20px;height:20px;border-radius:50%;background:var(--orange-bright);display:flex;align-items:center;justify-content:center}
.dots{position:absolute;left:214px;bottom:10px;display:flex;gap:3px}
.dots i{width:6px;height:6px;border-radius:50%;background:#c7c7c7}
.dots i:first-child{background:var(--orange-bright)}

/* services */
.services{left:89px;top:556px;width:711px;height:706px;background:var(--orange-bright)}
.services .tab{left:20px;top:0;height:41px}
.card{position:absolute;width:329px;background:var(--white);display:flex}
.card-photo{width:128px;flex:none}
.card-body{position:relative;flex:1;padding:38px 20px 0 11px;overflow:hidden}
.card-num{position:absolute;left:0;top:0;width:30px;height:30px;background:var(--dark);color:var(--white);font-family:"Dosis",sans-serif;font-weight:400;font-size:12px;display:flex;align-items:center;justify-content:center}
.card-title{position:absolute;left:38px;top:8px;right:10px;font-family:"Dosis",sans-serif;font-weight:400;font-size:12px;line-height:14px;color:#222;text-transform:uppercase}
.card-text{font-size:7.2px;line-height:9.6px;color:var(--text);text-align:justify}
.card-text p{margin-bottom:6px}
.card-bar{position:absolute;right:10px;width:4px;background:#bbbbbb}
.card-bar::before{content:"";position:absolute;left:0;top:0;width:4px;height:55%;background:var(--dark)}

/* footer */
.footer-links{left:89px;top:1278px;display:flex;font-size:7.5px;color:#b5b5b5}
.footer-links span{padding:0 12px;border-left:1px solid #777}
.footer-links span:first-child{padding-left:0;border-left:0}
.copyright{right:89px;top:1278px;font-size:7.5px;color:#b5b5b5}
</style>
</head>
<body>
<div class="stage">

  <header>
    <div class="abs brand">Vantage<br>Relations</div>
    <div class="abs phone">
      <span class="phone-icon"><svg width="12" height="12" viewBox="0 0 24 24"><path fill="#cfcfcf" d="M6.6 10.8a15 15 0 0 0 6.6 6.6l2.2-2.2a1 1 0 0 1 1-.3 11 11 0 0 0 3.6.6 1 1 0 0 1 1 1V20a1 1 0 0 1-1 1A17 17 0 0 1 3 4a1 1 0 0 1 1-1h3.5a1 1 0 0 1 1 1 11 11 0 0 0 .6 3.6 1 1 0 0 1-.3 1z"/></svg></span>
      +61 400 555 210
    </div>
    <nav class="abs nav">
      <a class="active">Home</a><a>Projects / Event</a><a>Client</a><a>Testimonials</a><a>Blog</a><a>Contact</a>
      <div class="social"><span>fb</span><span>tw</span><span>in</span></div>
    </nav>
  </header>

  <section class="hero">
    <div class="abs hero-photo" role="img" aria-label="Portrait of Dana Whitcombe in a sailing jacket"></div>
    <div class="abs hero-lead">
      <h1>Vantage Relations is an <b>established specialist public relations</b> and <b>event management business.</b></h1>
    </div>
    <div class="abs hero-copy">
      <p>With a communications degree and 20 plus years experience working in public relations, publicity, media and project management, VRL founder Dana Whitcombe offers a complete contract based option for your next major sporting, social, cultural or community event.</p>
      <p>Contact Dana at VRL for strategic advice on sponsorship spend and how to leverage your investment, and to tap into her extensive media and professional network.</p>
      <p>Flexible, composed and relationship focused freelancer ready to start work.</p>
    </div>
    <aside class="abs widget">
      <div class="widget-cover" role="img" aria-label="Page cover photo of yachts racing with colourful spinnakers">
        <div class="widget-avatar"></div>
        <div class="widget-title">VRL - Dana Whitcombe</div>
        <div class="widget-likes">410 likes</div>
        <div class="widget-btn" style="left:10px">Like Page</div>
        <div class="widget-btn" style="right:10px">Share</div>
      </div>
      <div class="widget-body">
        Be the first of your friends to like this
        <div class="friends"><i></i><i></i><i></i><i></i><i></i><i></i><i></i></div>
        <div class="post">
          <div class="post-avatar"></div>
          <div><div class="post-name">VRL - Dana Whitcombe</div><div style="font-size:6.5px;color:var(--muted)">7 hours ago</div></div>
        </div>
        <span class="post-sq"></span>
        <div class="post-text">A great initiative by Global Sail Federation, looking forward to listening in to panel members Mia Kerrow (left in pic) Tess Hallam Nina Varga &amp; I encourage all Australian yacht clubs to join the conversation</div>
      </div>
      <div class="widget-scroll"></div>
    </aside>
  </section>

  <section class="abs about">
    <div class="tab">ABOUT</div>
    <div class="about-text">
      <p>Dana grew up on Heron Island in the northern bay on Sydney's northern beaches, the breeding ground for many Australian sailing greats including the Harlands, Keoghs and the Marrows.</p>
      <p>As a 'tinny terror' she attended Harbourside Public School then Northshore High School with some of these sailing families, and now through her work she's back mingling with the greats.</p>
      <p>A communications degree at Ridgeway University, a career that has seen her rise to the top of her specialist field and three children later has brought her full circle back to the island as a home owner.</p>
      <p>Sailing-wise the women's twilight at the local club keeps her busy on the water each week.</p>
    </div>
    <div class="scrollbar" style="left:212px;top:48px;height:140px"></div>
  </section>
  <div class="abs slider" role="img" aria-label="Slideshow photo of a crowded marina with race flags and yacht masts">
    <span class="arrow" style="left:12px"><svg width="8" height="8" viewBox="0 0 8 8"><path d="M5.5 1 2.5 4l3 3" stroke="#fff" stroke-width="1.6" fill="none"/></svg></span>
    <span class="arrow" style="right:12px"><svg width="8" height="8" viewBox="0 0 8 8"><path d="M2.5 1l3 3-3 3" stroke="#fff" stroke-width="1.6" fill="none"/></svg></span>
    <div class="dots"><i></i><i></i><i></i><i></i></div>
  </div>

  <section class="abs services">
    <div class="tab">SERVICES</div>

    <article class="card" style="left:21px;top:54px;height:158px">
      <div class="card-photo" role="img" aria-label="Surf lifesavers paddling boards through the waves" style="background:linear-gradient(#8fa7b3,#c5d1d3 45%,#d9473b 70%,#e9e9e9)"></div>
      <div class="card-body">
        <div class="card-num">01</div><h2 class="card-title">Sports media</h2>
        <div class="card-text"><p>VRL founder Dana Whitcombe has worked closely with Australian and international sports media since 1996.</p><p>Key events include the annual Global Sail Federation World Cup, Bayside Regatta Week, the Coastal Classic Yacht Race, Reef Island Race Week and the state surf open titles.</p><p>Dana has a thorough understanding of the media's requirements for a strong story angle.</p></div>
        <div class="card-bar" style="top:38px;height:110px"></div>
      </div>
    </article>

    <article class="card" style="left:361px;top:54px;height:158px">
      <div class="card-photo" role="img" aria-label="Fleet of yachts with spinnakers seen from above a waterfront" style="background:linear-gradient(#2e5f98,#5d86b8 50%,#6b4d3f 80%,#3b3b3b)"></div>
      <div class="card-body">
        <div class="card-num">02</div><h2 class="card-title">Publicity</h2>
        <div class="card-text"><p>Generating media publicity for both the event and its sponsor is one of Dana's key strengths and drivers.</p><p>She works with clients to establish objectives and target audiences then develops a PR/media plan to deliver on the brief, from long lead magazines and social media campaigns to short lead opportunities and the resulting coverage.</p></div>
        <div class="card-bar" style="top:38px;height:110px"></div>
      </div>
    </article>

    <article class="card" style="left:21px;top:223px;height:158px">
      <div class="card-photo" role="img" aria-label="Crew working on a racing catamaran at speed" style="background:linear-gradient(#b9c3cc,#7f8891 40%,#1f2a33 65%,#6ea4c4)"></div>
      <div class="card-body">
        <div class="card-num">03</div><h2 class="card-title">Sponsorship leverage</h2>
        <div class="card-text"><p>Dana has worked with many sponsors including premium brand clients Crestmark, Kestrel Motors and Norvane Australia.</p><p>Regardless of stature or spend, Dana will advise honestly on what the client can expect in terms of mainstream and specialist media coverage, but also look for other ways to reach target audiences via social media, local media, signage and cooperative partnerships.</p></div>
        <div class="card-bar" style="top:38px;height:110px"></div>
      </div>
    </article>

    <article class="card" style="left:361px;top:223px;height:158px">
      <div class="card-photo" role="img" aria-label="Team in red shirts walking through a cheering crowd" style="background:linear-gradient(#7d6a5e,#c8333a 50%,#9e2128 80%,#3a3a44)"></div>
      <div class="card-body">
        <div class="card-num">04</div><h2 class="card-title">Event management</h2>
        <div class="card-text"><p>From planning through to execution and follow up, VRL provides a complete service.</p><p>Skilled in broader event planning including signage, entertainment and photography through to the media component including media accreditation, press packs, designing a working media centre and being hands-on at the event.</p><p>VRL has a number of specialised subcontractors to call on if the event is significant in size.</p></div>
        <div class="card-bar" style="top:38px;height:110px"></div>
      </div>
    </article>

    <article class="card" style="left:21px;top:393px;height:122px">
      <div class="card-photo" role="img" aria-label="Sailing crew in caps on the dock with flags" style="background:linear-gradient(#c9c9cf,#e8e8ec 40%,#c9343f 60%,#3b3f4a)"></div>
      <div class="card-body">
        <div class="card-num">05</div><h2 class="card-title">Crisis management</h2>
        <div class="card-text"><p>Every event should have an emergency management plan.</p><p>Businesses, community organisations and sponsors who understand well ahead how they are going to communicate with their stakeholders, as well as the media, during a crisis will handle the situation far better.</p></div>
      </div>
    </article>

    <article class="card" style="left:361px;top:393px;height:122px">
      <div class="card-photo" role="img" aria-label="Sailors in team kit at a press event" style="background:linear-gradient(#6b6258,#3d3b3b 45%,#1c2a48 75%,#c2c2c8)"></div>
      <div class="card-body">
        <div class="card-num">06</div><h2 class="card-title">Social media</h2>
        <div class="card-text"><p>Dana can create the client's presence and supply or edit content for whichever medium the client nominates.</p></div>
      </div>
    </article>

    <article class="card" style="left:21px;top:526px;height:158px">
      <div class="card-photo" role="img" aria-label="Sailors standing beside a silver trophy" style="background:linear-gradient(90deg,#d0c8bd,#9a8f83 35%,#2b2b2b 60%,#e8e8e8)"></div>
      <div class="card-body" style="padding-top:52px">
        <div class="card-num">07</div><h2 class="card-title">Writing &amp; editing web, newsletter and magazine content</h2>
        <div class="card-text"><p>Dana has a Bachelor of Communications (PR/journalism) and has developed strong writing skills over a 20 year career with a string of published articles in magazine titles and online.</p><p>Her byline has appeared in:<br>* Open Water Monthly - boat reviews<br>* Harbour Deck magazine - regatta previews</p></div>
        <div class="card-bar" style="top:40px;height:108px"></div>
      </div>
    </article>

    <article class="card" style="left:361px;top:526px;height:158px">
      <div class="card-photo" role="img" aria-label="Marina full of yacht masts in front of city towers" style="background:linear-gradient(#9fb2c4,#d8dde2 40%,#7b8590 70%,#2d4a6a)"></div>
      <div class="card-body">
        <div class="card-num">08</div><h2 class="card-title">Storytelling</h2>
        <div class="card-text"><p>Over the years Dana has developed a knack for telling a good yarn.</p><p>She has worked alongside and interviewed a number of sailing's most colourful characters and Australia's most successful business leaders, who respond well to her manner and line of questioning and are open and forthcoming, resulting in a meaningful article with new insight into the person or subject.</p></div>
      </div>
    </article>
  </section>

  <footer>
    <div class="abs footer-links"><span>Home</span><span>Projects / Event</span><span>Client</span><span>Testimonials</span><span>Blog</span><span>Contact</span></div>
    <div class="abs copyright">Copyright © 2017 Vantage Relations &nbsp;|&nbsp; All rights reserved</div>
  </footer>
</div>
</body>
</html>
```